MediDesk 4.2 is web based clinic management software. We require 1 logo for the software product, login page design and landing page (patient queue) design. The design should include all elements required logo, icons , buttons and type faces. http://md2021.tralvonix.my/Default.aspxTest login : KQ417 password : 4826 Final output should be in psd for developer to convert to css for web application.

Number of Pages Required

1 page

Colors

Designer to choose colors to be used in the design.

Requirements
Must have
• Product Logo , icon, login page design, and 1 main page design as attached.

```html
<!DOCTYPE html>
<html lang="en">
<head>
<meta charset="utf-8">
<title>MediDesk 4.2 – Login and Patient Queue</title>
<link href="https://fonts.googleapis.com/css2?family=Poppins:wght@400;500;600;700&display=swap" rel="stylesheet">
<style>
:root{
  --navy:#0c2640;
  --blue:#1b4fa3;
  --blue-dark:#123f86;
  --green:#5aa022;
  --green-dark:#4a8c1a;
  --ink:#222;
  --muted:#555;
  --panel:#ebebeb;
  --foot:#f2f2f2;
  --line:#d6d6d6;
  --white:#fff;
}
*{box-sizing:border-box;margin:0;padding:0}
html,body{width:698px;height:1200px;overflow:hidden}
body{background:var(--navy);font-family:"Poppins",sans-serif;color:var(--ink);position:relative}
.page{position:absolute;left:82px;width:535px;background:var(--white);overflow:hidden}
.page--login{top:60px;height:531px}
.page--queue{top:624px;height:531px}
.site-header{position:absolute;left:0;top:0;width:100%;height:44px;background:var(--white)}
.brand{position:absolute;display:flex;align-items:center;gap:5px;font-weight:700;color:var(--blue);letter-spacing:.2px}
.brand__dot{width:12px;height:12px;border-radius:50%;background:var(--green)}
.site-header .brand{font-size:15px;top:13px}
.btn{position:absolute;display:flex;align-items:center;justify-content:center;gap:4px;border-radius:10px;font-size:8px;font-weight:600;text-transform:uppercase;border:1.2px solid}
.btn svg{width:8px;height:8px}
.btn--outline-green{color:var(--green);border-color:var(--green);background:var(--white)}
.btn--outline-blue{color:var(--blue);border-color:var(--blue);background:var(--white)}
.btn--solid-green{color:var(--white);background:var(--green);border-color:var(--green)}
.hero{position:absolute;left:0;top:44px;width:100%;height:276px}
.hero--photo{background:radial-gradient(circle at 25% 30%,rgba(120,180,230,.35),transparent 45%),linear-gradient(90deg,#1d5aa8 0%,#2a7a9a 45%,#4c9435 75%,#57972b 100%)}
.hero--stripes{background:linear-gradient(100deg,#1a5aa6 0%,#1f6f98 40%,#3c8a45 70%,#4e8f28 100%)}
.hero__art{position:absolute;inset:0}
.login-card{position:absolute;left:140px;top:50px;width:254px;height:169px;background:var(--panel)}
.login-card .brand{font-size:22px;left:50%;transform:translateX(-50%);top:24px}
.login-card .brand__dot{width:16px;height:16px}
.field{position:absolute;left:22px;width:210px;height:20px;background:var(--white);border:1px solid var(--line);border-radius:2px;font-size:6px;color:var(--muted);padding:0 6px;display:flex;align-items:center}
.login-card .btn{top:135px;width:50px;height:16px;border-radius:8px}
.site-footer{position:absolute;left:0;top:320px;width:100%;height:174px;background:var(--foot)}
.footer-col{position:absolute;top:28px}
.footer-col h3{font-size:10.5px;font-weight:700;letter-spacing:.3px;margin-bottom:13px}
.contact{left:63px;width:160px}
.contact .company{font-size:7px;line-height:11px;font-weight:500;margin-bottom:7px}
.contact-item{display:flex;gap:6px;font-size:6.4px;line-height:10px;margin-bottom:4px;color:#333}
.contact-item svg{flex:0 0 8px;width:8px;height:8px;margin-top:1px;fill:var(--blue)}
.links{left:253px}
.links ul{list-style:none;font-size:5.6px;line-height:10.8px;color:#333}
.links li::before{content:"▸";font-size:5px;margin-right:4px}
.follow{left:363px}
.social{display:flex;gap:3px}
.social span{width:12px;height:12px;border-radius:50%;border:1px solid #777}
.copyright{position:absolute;left:0;bottom:0;width:100%;height:37px;display:flex;align-items:center;justify-content:center;font-size:6.5px;color:#333;background:var(--white)}
.menu-toggle{position:absolute;left:64px;top:16px;width:15px;height:12px;display:flex;flex-direction:column;justify-content:space-between}
.menu-toggle span{height:2.4px;background:var(--blue);border-radius:1px}
.page--queue .site-header .brand{left:50%;transform:translateX(-50%)}
.filter-panel{position:absolute;left:51px;top:74px;width:433px;height:90px;background:var(--panel)}
.clock{position:absolute;right:26px;top:10px;font-size:7px;color:var(--blue);font-weight:500}
.label{position:absolute;top:23px;font-size:6.8px;color:#333}
.filter-panel .field{top:37px;width:181px;height:18px;left:32px;border-radius:1px}
.filter-panel .field--select{left:225px;justify-content:space-between}
.filter-panel .field--select::after{content:"";border:2.5px solid transparent;border-top:3px solid #333;margin-top:3px}
.show-all{position:absolute;left:287px;top:68px;display:flex;align-items:center;gap:4px;font-size:5.6px;font-weight:500;text-transform:uppercase}
.show-all i{width:6px;height:6px;border:1px solid #555}
.filter-panel .btn{left:355px;top:64px;width:50px;height:15px;border-radius:1px}
.queue-panel{position:absolute;left:51px;top:170px;width:433px;height:128px;background:var(--white)}
.queue-panel h2{position:absolute;left:8px;top:11px;font-size:11px;font-weight:700;color:var(--blue);letter-spacing:.3px}
.queue-panel .sub{position:absolute;left:9px;top:27px;font-size:6.8px;color:#333;border-left:2px solid var(--blue);padding-left:4px;line-height:10px}
.queue-table{position:absolute;left:9px;top:46px;width:416px;border-collapse:collapse;table-layout:fixed;font-size:6.4px}
.queue-table th{background:var(--panel);height:26px;color:var(--blue);font-weight:600;text-align:left;padding-left:10px}
.queue-table td{height:26px;border-bottom:1px solid var(--line);padding-left:10px;color:#333;white-space:nowrap}
.icons{display:flex;gap:2px;align-items:center}
.icons svg{width:8px;height:8px;fill:#333}
.actions{display:flex;gap:14px;align-items:center;padding-left:10px}
.actions svg{width:9px;height:9px;fill:#333}
.pager{position:absolute;left:9px;top:105px;display:flex;align-items:center;gap:7px;font-size:6.8px;color:#333}
.pager .rows{width:29px;height:12px;border:1px solid var(--line);font-size:5.8px;padding-left:3px;display:flex;align-items:center}
</style>
</head>
<body>

<section class="page page--login">
  <header class="site-header">
    <div class="brand" style="left:64px"><span class="brand__dot"></span>MediDesk</div>
    <span class="btn btn--outline-green" style="left:340px;top:14px;width:58px;height:18px">
      <svg viewBox="0 0 10 10"><rect x="1.5" y="4.5" width="7" height="5" rx="1" fill="currentColor"/><path d="M3 4.5V3a2 2 0 0 1 4 0" fill="none" stroke="currentColor" stroke-width="1.3"/></svg>Login</span>
    <span class="btn btn--outline-blue" style="left:404px;top:14px;width:66px;height:18px">
      <svg viewBox="0 0 10 10"><rect x="1" y="2" width="7" height="7" fill="none" stroke="currentColor" stroke-width="1.2"/><path d="M4 6l5-5" stroke="currentColor" stroke-width="1.4"/></svg>Sign up</span>
  </header>
  <div class="hero hero--photo">
    <div class="hero__art" role="img" aria-label="Clinical photograph of a doctor at work with a glowing molecular network overlay, in blue and green tones"></div>
    <form class="login-card">
      <div class="brand"><span class="brand__dot"></span>MediDesk</div>
      <div class="field" style="top:78px">Username</div>
      <div class="field" style="top:103px">Password</div>
      <span class="btn btn--outline-blue" style="left:74px">Clear</span>
      <span class="btn btn--solid-green" style="left:130px">Login</span>
    </form>
  </div>
  <footer class="site-footer">
    <div class="footer-col contact">
      <h3>CONTACT US</h3>
      <p class="company">KELVARA SYSTEMS (MSC) SDN BHD<br>TRM KELVARA SYSTEMS SDN BHD</p>
      <div class="contact-item"><svg viewBox="0 0 10 10"><path d="M5 0a3.5 3.5 0 0 0-3.5 3.5C1.5 6 5 10 5 10s3.5-4 3.5-6.5A3.5 3.5 0 0 0 5 0zm0 5a1.5 1.5 0 1 1 0-3 1.5 1.5 0 0 1 0 3z"/></svg><span>No. 22, Block C2, Jalan Meranti 4/7, Seri Indah Business Park, 47300 Petaling Jaya, Selangor, Malaysia</span></div>
      <div class="contact-item"><svg viewBox="0 0 10 10"><path d="M2 0l2 2.5-1 1.5a6 6 0 0 0 3 3l1.5-1L10 8l-1.5 2C4 10 0 6 0 1.5z"/></svg><span>Tel: +603 5521 8840 , +6012 4183 376</span></div>
      <div class="contact-item"><svg viewBox="0 0 10 10"><rect x="0" y="3" width="10" height="7" rx="1"/><rect x="2" y="0" width="6" height="3"/></svg><span>Fax: 03 -5521 8841</span></div>
      <div class="contact-item"><svg viewBox="0 0 10 10"><path d="M0 2h10v6H0z M0 2l5 3.5L10 2" /></svg><span>Email : hello@kelvara.my</span></div>
    </div>
    <div class="footer-col links"><h3>QUICK LINKS</h3><ul><li>Link 1</li><li>Link 2</li><li>Link 3</li><li>Link 4</li></ul></div>
    <div class="footer-col follow"><h3>FOLLOW US</h3><div class="social"><span></span><span></span><span></span><span></span></div></div>
  </footer>
  <p class="copyright">MediDesk © 2018 All Rights Reserved | Privacy Policy | Terms and Conditions</p>
</section>

<section class="page page--queue">
  <header class="site-header">
    <div class="menu-toggle"><span></span><span></span><span></span></div>
    <div class="brand"><span class="brand__dot"></span>MediDesk</div>
    <span class="btn btn--outline-green" style="left:412px;top:14px;width:58px;height:18px">
      <svg viewBox="0 0 10 10"><rect x="1.5" y="4.5" width="7" height="5" rx="1" fill="currentColor"/><path d="M3 4.5V3a2 2 0 0 1 4 0" fill="none" stroke="currentColor" stroke-width="1.3"/></svg>Logout</span>
  </header>
  <div class="hero hero--stripes">
    <div class="hero__art" role="img" aria-label="Diagonal line texture band shading from blue to green"></div>
  </div>
  <form class="filter-panel">
    <p class="clock">7:49 PM, 20 NOVEMBER 2018</p>
    <span class="label" style="left:32px">Queue Date</span>
    <span class="label" style="left:225px">Location</span>
    <div class="field">20-Oct-2018</div>
    <div class="field field--select">All Facilities</div>
    <label class="show-all"><i></i>Show all status</label>
    <span class="btn btn--solid-green">Login</span>
  </form>
  <section class="queue-panel">
    <h2>QUEUE LIST</h2>
    <p class="sub">Listing of patients in queue.(1 result)</p>
    <table class="queue-table">
      <colgroup><col style="width:67px"><col style="width:87px"><col style="width:34px"><col style="width:36px"><col style="width:47px"><col style="width:56px"><col style="width:89px"></colgroup>
      <thead><tr><th>NO</th><th>PATIENT NAME</th><th>TIME</th><th>PAYOR</th><th>AMOUNT</th><th>DOCTOR</th><th>LOCATION</th></tr></thead>
      <tbody><tr>
        <td><span class="icons">
          <svg viewBox="0 0 10 10"><circle cx="5" cy="3" r="2.2"/><path d="M1 10a4 4 0 0 1 8 0z"/></svg>
          <svg viewBox="0 0 10 10"><path d="M2 5V2.5h1V5h.5V1h1v4H5V1.5h1V5h.5V3h1v4A3 3 0 0 1 2 7z"/></svg>
          <svg viewBox="0 0 10 10"><path d="M0 2h10v6H0zm1 1v4h8V3z"/><circle cx="5" cy="5" r="1.3"/></svg>
          <svg viewBox="0 0 10 10"><path d="M2 0h4l2 2v8H2zm1 1v8h4V3H5V1z"/></svg>
        </span></td>
        <td>Hafiz Rahman&nbsp; 26 ♂</td>
        <td>09:01am</td>
        <td><svg viewBox="0 0 10 10" width="7" height="7"><rect x="2" y="0" width="6" height="10" fill="#333"/></svg></td>
        <td>Rm2,473.12</td>
        <td>000178</td>
        <td style="padding-left:0"><span class="actions">
          <svg viewBox="0 0 10 10"><path d="M1 0h8v1H8c0 2-2 3-2 4s2 2 2 4h1v1H1V9h1c0-2 2-3 2-4S2 3 2 1H1z"/></svg>
          <svg viewBox="0 0 10 10"><path d="M5 1a4 4 0 1 1-4 4h1.2A2.8 2.8 0 1 0 5 2.2V4L2.5 1.6 5 0z"/><path d="M4.5 3h1v2.3l1.5 1-.6.8-1.9-1.3z"/></svg>
          <svg viewBox="0 0 10 10"><path d="M0 2h5v1H1v6h6V5h1v5H0z"/><path d="M8.5 0L10 1.5 5 6.5H3.5V5z"/></svg>
          <svg viewBox="0 0 10 10"><circle cx="5" cy="3" r="2.2"/><path d="M1 10a4 4 0 0 1 8 0z"/></svg>
        </span></td>
      </tr></tbody>
    </table>
    <div class="pager">Rows per page: <span class="rows">10 ⌄</span> Page 1 of 1 &nbsp;‹ &nbsp;›</div>
  </section>
  <footer class="site-footer" style="top:320px">
    <div class="footer-col contact">
      <h3>CONTACT US</h3>
      <p class="company">KELVARA SYSTEMS (MSC) SDN BHD<br>TRM KELVARA SYSTEMS SDN BHD</p>
      <div class="contact-item"><svg viewBox="0 0 10 10"><path d="M5 0a3.5 3.5 0 0 0-3.5 3.5C1.5 6 5 10 5 10s3.5-4 3.5-6.5A3.5 3.5 0 0 0 5 0zm0 5a1.5 1.5 0 1 1 0-3 1.5 1.5 0 0 1 0 3z"/></svg><span>No. 22, Block C2, Jalan Meranti 4/7, Seri Indah Business Park, 47300 Petaling Jaya, Selangor, Malaysia</span></div>
      <div class="contact-item"><svg viewBox="0 0 10 10"><path d="M2 0l2 2.5-1 1.5a6 6 0 0 0 3 3l1.5-1L10 8l-1.5 2C4 10 0 6 0 1.5z"/></svg><span>Tel: +603 5521 8840 , +6012 4183 376</span></div>
      <div class="contact-item"><svg viewBox="0 0 10 10"><rect x="0" y="3" width="10" height="7" rx="1"/><rect x="2" y="0" width="6" height="3"/></svg><span>Fax: 03 -5521 8841</span></div>
      <div class="contact-item"><svg viewBox="0 0 10 10"><path d="M0 2h10v6H0z M0 2l5 3.5L10 2" /></svg><span>Email : hello@kelvara.my</span></div>
    </div>
    <div class="footer-col links"><h3>QUICK LINKS</h3><ul><li>Link 1</li><li>Link 2</li><li>Link 3</li><li>Link 4</li></ul></div>
    <div class="footer-col follow"><h3>FOLLOW US</h3><div class="social"><span></span><span></span><span></span><span></span></div></div>
  </footer>
  <p class="copyright">MediDesk © 2018 All Rights Reserved | Privacy Policy | Terms and Conditions</p>
</section>

</body>
</html>
```